Sticker Design

Wanting business name across the bottom of car doors, please see attached. looking for something simple and require asap. Happy for black and white simple colouring.

Thank you
Brent Mallory

```html
<!DOCTYPE html>
<html lang="en">
<head>
<meta charset="utf-8">
<title>Field Service and Logistics – Door Sticker</title>
<link href="https://fonts.googleapis.com/css2?family=Michroma&family=Montserrat:wght@700&display=swap" rel="stylesheet">
<style>
  :root {
    --ink: #0b0b0b;
    --paper: #ffffff;
    --backdrop: #e6e8eb;
    --rule: #8a8a8a;
  }
  html, body {
    margin: 0;
    padding: 0;
    overflow: hidden;
  }
  .canvas {
    position: relative;
    width: 1200px;
    height: 1200px;
    background: var(--backdrop);
    overflow: hidden;
  }
  .sticker {
    position: absolute;
    left: 0;
    top: 560px;
    width: 1200px;
    height: 81px;
    background: var(--paper);
  }
  .sticker-shapes {
    position: absolute;
    inset: 0;
    width: 100%;
    height: 100%;
  }
  .service-line {
    position: absolute;
    left: 142px;
    top: 12px;
    width: 600px;
    margin: 0;
    font-family: "Michroma", sans-serif;
    font-size: 21px;
    line-height: 1;
    letter-spacing: 1.5px;
    word-spacing: 10px;
    color: var(--paper);
    white-space: nowrap;
    text-align: center;
  }
  .phone {
    position: absolute;
    left: 296px;
    top: 44px;
    margin: 0;
    font-family: "Montserrat", sans-serif;
    font-weight: 700;
    font-size: 25px;
    line-height: 1;
    letter-spacing: 6px;
    color: var(--paper);
    white-space: nowrap;
  }
  .brand {
    position: absolute;
    left: 842px;
    top: 10px;
    margin: 0;
    font-family: "Michroma", sans-serif;
    font-size: 58px;
    line-height: 1;
    letter-spacing: 4px;
    color: var(--ink);
    white-space: nowrap;
  }
</style>
</head>
<body>
  <main class="canvas">
    <section class="sticker" aria-label="Door sticker">
      <svg class="sticker-shapes" viewBox="0 0 1200 81" preserveAspectRatio="none" aria-hidden="true">
        <polygon class="stripe" points="2,0 30,0 92,81 66,81" fill="var(--ink)"/>
        <polygon class="stripe" points="38,0 66,0 128,81 102,81" fill="var(--ink)"/>
        <polygon class="band" points="80,0 828,0 810,81 146,81" fill="var(--ink)"/>
        <line class="band-rule" x1="196" y1="34.5" x2="690" y2="34.5" stroke="var(--rule)" stroke-width="1"/>
      </svg>
      <p class="service-line">FIELD SERVICE AND LOGISTICS</p>
      <p class="phone">0412 555 208</p>
      <p class="brand">TRK</p>
    </section>
  </main>
</body>
</html>
```